Need a business letterhead for word docs

Hi, I need a business letterhead. We have had some before but they have issues printing them. I have attached a sample of what we have used that I want improved :) and a PSD of our logo, please use the one with all caps. This will be used for all our correspondance with clients and profeesionals. Our client base are children, so these documents will go to their parents and doctors and paediatricians who also treat these children.

Target Market(s)

Clients (who are families and children) and doctors/paediatricians

Industry/Entity Type

Health Care

Font styles to use
Sans Serif

Colors
85cae6

Requirements
Must have
• My logo and the feel of my logo
Nice to have
• clean feel

```html
<!DOCTYPE html>
<html lang="en">
<head>
<meta charset="utf-8">
<title>Bright Sprout Letterhead</title>
<link rel="stylesheet" href="https://fonts.googleapis.com/css2?family=Fira+Sans:ital,wght@0,400;0,500;0,600;1,400;1,600&display=swap">
<style>
  :root {
    --paper: #ffffff;
    --brand-blue: #0a80c6;
    --band-blue: #1a90cd;
    --sky: #85cae6;
    --text-grey: #8c8c8c;
    --text-light: #a9a9a9;
    --rule-grey: #9a9a9a;
  }
  * { margin: 0; padding: 0; box-sizing: border-box; }
  html, body {
    width: 927px;
    height: 1200px;
    overflow: hidden;
    background: var(--paper);
  }
  .letterhead {
    position: relative;
    width: 927px;
    height: 1200px;
    background: var(--paper);
    font-family: "Fira Sans", sans-serif;
  }
  .brand {
    position: absolute;
    top: 160px;
    right: 54px;
    display: flex;
    align-items: center;
    gap: 14px;
  }
  .brand-dot {
    width: 30px;
    height: 30px;
    border-radius: 50%;
    background: var(--sky);
  }
  .brand-name {
    font-family: "Fira Sans", sans-serif;
    font-weight: 600;
    font-size: 38px;
    letter-spacing: 0.5px;
    color: var(--brand-blue);
    line-height: 1;
  }
  .edge-band {
    position: absolute;
    top: 1093px;
    width: 22px;
    height: 75px;
    background: var(--band-blue);
  }
  .edge-band--left { left: 0; }
  .edge-band--right { right: 0; }
  .contact-strip {
    position: absolute;
    top: 1106px;
    left: 0;
    width: 927px;
    height: 54px;
  }
  .contact-item {
    position: absolute;
    font-style: italic;
    font-size: 14px;
    line-height: 18px;
    color: var(--text-grey);
    white-space: nowrap;
  }
  .contact-item--address { left: 84px; top: 8px; }
  .contact-item--centre { left: 249px; top: 0; color: var(--text-light); }
  .contact-item--fax { left: 413px; top: 8px; }
  .contact-item--phone { left: 546px; top: 8px; }
  .contact-item--email { left: 677px; top: 8px; }
  .contact-heading {
    font-weight: 600;
    color: var(--text-grey);
  }
  .contact-divider {
    position: absolute;
    top: 2px;
    width: 2px;
    height: 48px;
    background: var(--rule-grey);
  }
</style>
</head>
<body>
  <main class="letterhead">
    <header class="brand">
      <span class="brand-dot" aria-hidden="true"></span>
      <span class="brand-name">BRIGHT SPROUT</span>
    </header>

    <div class="edge-band edge-band--left" aria-hidden="true"></div>
    <div class="edge-band edge-band--right" aria-hidden="true"></div>

    <footer class="contact-strip">
      <p class="contact-item contact-item--address">48 Tallow Lane<br>Elmhurst 3142</p>
      <span class="contact-divider" style="left:221px"></span>
      <p class="contact-item contact-item--centre"><span class="contact-heading">Therapy Centre</span><br>9 Finch Parade<br>Kestrel Bay 3197</p>
      <span class="contact-divider" style="left:389px"></span>
      <p class="contact-item contact-item--fax">Fax<br>03 9410 2257</p>
      <span class="contact-divider" style="left:523px"></span>
      <p class="contact-item contact-item--phone">Telephone<br>03 9410 2255</p>
      <span class="contact-divider" style="left:654px"></span>
      <p class="contact-item contact-item--email">E-mail<br>hello@brightsproutclinic.com.au</p>
    </footer>
  </main>
</body>
</html>
```